Wealth management firm needs a business card design

Using my logo, create a business card that covers all of the regulatory wordings that I need. It must have - Registered Office 7-9 Pelgrove Wynd, Edinburgh, EH4 2QN. Registered in Scotland under number SC804317. VORELT Wealth Management Ltd is an appointed representative of Kestoby wealth management Ltd, which is authorised and regulated by the Monetary Oversight Council.

Target Market(s)

professional clients

Industry/Entity Type

finance

Contact Information for Business Card

VORELT Wealth Management, Conor Tresk-Whitlaw, Director, 5 Dunmore Row, Edinburgh, EH9 4RT. 07812 459 163, conor.tresk-whitlaw@vorelt-example.com , www.vorelt-example.com

Font styles to use
Serif

Colors
0054AA
0677BA
7BADD7
CADEEF
E8F1F8

Requirements
Must have
• regulatory wording in small text at bottom

```html
<!DOCTYPE html>
<html lang="en">
<head>
<meta charset="utf-8">
<title>VORELT Wealth Management – Business Card</title>
<link rel="stylesheet" href="https://fonts.googleapis.com/css2?family=Noto+Serif:wght@400;700&family=Arimo:wght@400&display=swap">
<style>
  :root {
    --navy: #1e1f29;
    --blue: #0677ba;
    --bright-blue: #0a78e6;
    --deep-blue: #0054aa;
    --soft-blue: #7badd7;
    --pale-blue: #cadeef;
    --mist: #e8f1f8;
    --paper: #f6f6f7;
    --ink: #1a1a1a;
    --backdrop: #d9dbe0;
    --white: #ffffff;
  }
  * { margin: 0; padding: 0; box-sizing: border-box; }
  html, body { width: 1200px; height: 960px; overflow: hidden; }
  body {
    background: var(--backdrop);
    position: relative;
    font-family: "Noto Serif", Georgia, serif;
  }
  .card {
    position: absolute;
    left: 250px;
    width: 700px;
    height: 400px;
    border-radius: 26px;
    overflow: hidden;
    box-shadow: 0 10px 30px rgba(0,0,0,0.18);
  }
  /* Back of card */
  .card--back {
    top: 40px;
    background: var(--navy);
    color: var(--white);
    text-align: center;
  }
  .brand {
    display: flex;
    align-items: center;
    justify-content: center;
    gap: 14px;
  }
  .brand__dot {
    border-radius: 50%;
    background: var(--bright-blue);
    flex: none;
  }
  .card--back .brand { margin-top: 92px; }
  .card--back .brand__dot { width: 34px; height: 34px; }
  .card--back .brand__name {
    font-size: 34px;
    font-weight: 700;
    letter-spacing: 0.5px;
  }
  .tagline {
    font-size: 13px;
    letter-spacing: 0.6px;
    margin-top: 4px;
  }
  .regulatory {
    font-size: 15.5px;
    font-weight: 700;
    line-height: 1.35;
    margin: 38px auto 0;
    width: 600px;
  }
  .rule {
    width: 64px;
    height: 2px;
    background: var(--bright-blue);
    margin: 10px auto;
  }
  .registered {
    font-size: 14px;
    line-height: 1.45;
    width: 600px;
    margin: 0 auto;
  }

  /* Front of card */
  .card--front {
    top: 520px;
    background: var(--paper);
    color: var(--ink);
  }
  .front__logo {
    position: absolute;
    left: 60px;
    top: 38px;
    width: 300px;
    text-align: center;
  }
  .front__logo .brand__dot { width: 22px; height: 22px; }
  .front__logo .brand__name {
    font-size: 19px;
    font-weight: 400;
  }
  .front__logo .tagline { font-size: 8px; margin-top: 2px; }
  .contact {
    position: absolute;
    left: 44px;
    top: 132px;
    font-family: "Arimo", Arial, sans-serif;
    font-size: 17px;
    line-height: 1.3;
  }
  .contact__name {
    font-family: "Noto Serif", Georgia, serif;
    font-weight: 700;
    font-size: 27px;
    color: var(--bright-blue);
    line-height: 1.15;
  }
  .contact__role { font-size: 19px; }
  .contact__email { font-size: 15px; margin-bottom: 14px; }
  .contact__address { font-size: 18px; margin-bottom: 12px; }
  .contact__line {
    display: flex;
    align-items: center;
    gap: 10px;
    font-size: 18px;
  }
  .contact__line svg { width: 16px; height: 16px; flex: none; }
  .front__decoration {
    position: absolute;
    right: 0;
    top: 0;
    width: 300px;
    height: 400px;
    background: radial-gradient(circle at 55% 45%, var(--bright-blue) 0%, var(--soft-blue) 45%, var(--pale-blue) 75%, var(--paper) 100%);
  }
</style>
</head>
<body>

<section class="card card--back" aria-label="Back of business card">
  <div class="brand">
    <span class="brand__dot"></span>
    <span class="brand__name">VORELT Wealth Management Ltd</span>
  </div>
  <p class="tagline">Personal Financial Advice</p>
  <p class="regulatory">VORELT Wealth Management Ltd is an appointed representative of Kestoby wealth management Ltd, which is authorised and regulated by the Monetary Oversight Council.</p>
  <div class="rule"></div>
  <p class="registered">Registered Office: 7-9 Pelgrove Wynd, Edinburgh, EH4 2QN.<br>Registered in Scotland under number SC804317.</p>
</section>

<section class="card card--front" aria-label="Front of business card">
  <div class="front__logo">
    <div class="brand">
      <span class="brand__dot"></span>
      <span class="brand__name">VORELT Wealth Management Ltd</span>
    </div>
    <p class="tagline">Personal Financial Advice</p>
  </div>

  <div class="contact">
    <p class="contact__name">Conor Tresk-Whitlaw</p>
    <p class="contact__role">Director</p>
    <p class="contact__email">conor.tresk-whitlaw@vorelt-example.com</p>
    <p class="contact__address">5 Dunmore Row, Edinburgh<br>EH9 4RT.</p>
    <p class="contact__line">
      <svg viewBox="0 0 24 24" aria-hidden="true"><path fill="#0a78e6" d="M6.6 10.8a15.1 15.1 0 0 0 6.6 6.6l2.2-2.2a1 1 0 0 1 1-.25 11.4 11.4 0 0 0 3.6.57 1 1 0 0 1 1 1V20a1 1 0 0 1-1 1A17 17 0 0 1 3 4a1 1 0 0 1 1-1h3.5a1 1 0 0 1 1 1c0 1.25.2 2.45.57 3.57a1 1 0 0 1-.25 1z"/></svg>
      07812 459 163
    </p>
    <p class="contact__line">
      <svg viewBox="0 0 24 24" aria-hidden="true"><circle cx="12" cy="12" r="10" fill="#0a78e6"/><path d="M2 12h20M12 2c3 3 3 17 0 20M12 2c-3 3-3 17 0 20" stroke="#f6f6f7" stroke-width="1.5" fill="none"/></svg>
      www.vorelt-example.com
    </p>
  </div>

  <div class="front__decoration" role="img" aria-label="Decorative pattern of blue dots"></div>
</section>

</body>
</html>
```